Rice importer and exporter. We need a new design for a 18 kg plastic bag.

We want to create a new brand of rice. This type of rice is produced in southeast Asia, imported to Portugal and sold to the local market. The target are people 30+ years old of all ethnicity. The name of the brand should be 'Kavrel', this is the name we want people to see and get used to it. <br/>Regarding the package itself. We want a simple bag, not with many different colours (3, 4 or 5) with preference to golden yellow. The Front page, should have our brand 'Kavrel' and the exact description of the type of rice 'Arroz 100% Jasmin Perfumado' and 'Premium Quality'. In the bag should also be included the nutrition facts, cooking instructions, a trasnparent part where customer can see the quality of the product and the our company info. Finally we would like to see in the front page the five stars and on the back the triple AAA (see examples of attached files). All the remaining should be of your imagination. <br/>Finally, the image 3 is an example of a bag structure that we want to make.

Target Market(s)

People 30+ years old

Font styles to use
Serif
Sans Serif

Colors
ffc214
fec214
fee18a
fbee3f
faef58
fbf289

Requirements
Must have
• 5 Stars on the front page, triple A's on the back and a transparent area for the customers to see the quality of the rice.

```html
<!DOCTYPE html>
<html lang="pt">
<head>
<meta charset="utf-8">
<title>Kavrel – Arroz 100% Jasmin Perfumado – Bag Design</title>
<link rel="stylesheet" href="https://fonts.googleapis.com/css2?family=Nunito:ital,wght@0,400;0,700;0,800;0,900;1,800&family=Merriweather:ital,wght@1,900&display=swap">
<style>
  :root{
    --gold:#ffc214;
    --gold-2:#fec214;
    --gold-light:#fee18a;
    --lemon:#fbee3f;
    --lemon-2:#faef58;
    --pale:#fbf289;
    --brown:#6b3a12;
    --brown-dark:#4a260a;
    --cream:#f7efd9;
    --stage:#f1f1f1;
  }
  *{box-sizing:border-box;margin:0;padding:0}
  html,body{width:1200px;height:1136px;overflow:hidden;background:var(--stage)}
  body{position:relative;font-family:"Nunito",Arial,sans-serif;color:var(--brown)}

  .panel{position:absolute;top:138px;width:540px;height:860px;border-radius:6px;overflow:hidden;
    background:linear-gradient(160deg,var(--pale) 0%,var(--lemon) 30%,var(--gold) 75%,var(--gold-2) 100%);
    box-shadow:0 4px 14px rgba(0,0,0,.12)}
  .panel--front{left:40px}
  .panel--back{left:620px}
  .frame{position:absolute;inset:18px;border:5px solid var(--brown);border-radius:16px}

  /* front */
  .ribbon{position:absolute;left:50%;top:40px;transform:translateX(-50%);width:260px;height:40px;
    background:var(--brown);clip-path:polygon(0 0,100% 0,94% 50%,100% 100%,0 100%,6% 50%);
    display:flex;align-items:center;justify-content:center}
  .ribbon__text{font-family:"Merriweather",Georgia,serif;font-style:italic;font-weight:900;font-size:19px;color:var(--lemon)}
  .stars{position:absolute;left:0;right:0;top:100px;display:flex;justify-content:center;gap:6px}
  .stars svg{width:26px;height:26px}
  .brand{position:absolute;left:0;right:0;top:128px;text-align:center;font-weight:900;font-size:96px;line-height:1;color:var(--brown);letter-spacing:1px}
  .brand__dot{display:inline-block;width:18px;height:18px;border-radius:50%;background:var(--brown);vertical-align:middle;margin-left:8px}
  .descriptor{position:absolute;left:50%;top:250px;transform:translateX(-50%);white-space:nowrap;
    padding:8px 18px;border:3px solid var(--brown);border-radius:6px;background:var(--gold-light);
    font-weight:900;font-size:23px;color:var(--brown)}
  .dragon-art{position:absolute;left:170px;top:330px;width:200px;height:110px;border-radius:40px;
    background:radial-gradient(ellipse at center,rgba(107,58,18,.45),rgba(107,58,18,.08) 70%,transparent)}
  .dish-photo{position:absolute;left:60px;top:520px;width:300px;height:140px;border-radius:50%;
    background:radial-gradient(ellipse at 50% 45%,#f6f1e4 0%,#e9dfc6 55%,#cfc3a5 100%);
    box-shadow:0 6px 12px rgba(0,0,0,.18)}
  .window{position:absolute;left:23px;right:23px;bottom:23px;height:270px}
  .window svg{width:100%;height:100%;display:block}

  /* back */
  .map-art{position:absolute;left:44px;top:46px;width:230px;height:210px;border-radius:18px;
    background:radial-gradient(ellipse at 45% 55%,#8da04a 0%,#b7a548 45%,rgba(255,194,20,0) 75%)}
  .nutrition{position:absolute;right:42px;top:44px;width:200px;background:#fff;border:2px solid var(--brown-dark);
    font-size:10.5px;color:#222;border-collapse:collapse}
  .nutrition caption{background:var(--brown-dark);color:#fff;font-weight:900;font-size:13px;padding:4px;letter-spacing:.5px}
  .nutrition td{border-top:1px solid #999;padding:3px 6px}
  .nutrition td:last-child{text-align:right;font-weight:700}
  .nutrition .per td{font-weight:800;border-top:none}

  .steps{position:absolute;left:44px;right:42px;top:340px;display:grid;grid-template-columns:1fr 1fr;gap:12px 16px}
  .step{display:flex;gap:8px;align-items:center;background:var(--gold-light);border:2px solid var(--brown);border-radius:6px;padding:6px 8px;height:58px}
  .step__num{flex:0 0 24px;height:24px;border-radius:50%;background:var(--brown);color:var(--lemon);font-weight:900;font-size:13px;display:flex;align-items:center;justify-content:center}
  .step__text{font-size:12px;font-weight:700;line-height:1.2;color:var(--brown-dark)}

  .storage-note{position:absolute;right:42px;top:580px;width:220px;font-size:12px;font-weight:700;line-height:1.35;color:var(--brown-dark)}
  .origin{position:absolute;right:42px;top:650px;width:220px;font-size:12px;font-weight:800;color:var(--brown-dark)}
  .company{position:absolute;left:44px;top:600px;width:220px;padding:10px 12px;background:var(--brown);border-radius:6px;color:var(--gold-light);font-size:12px;line-height:1.45}
  .company__name{font-weight:900;font-size:13px}
  .grade{position:absolute;right:42px;bottom:44px;width:120px;height:58px;background:var(--lemon);border:3px solid var(--brown);border-radius:4px;
    display:flex;align-items:center;justify-content:center;font-weight:900;font-size:34px;color:var(--brown-dark);letter-spacing:2px}
</style>
</head>
<body>

<section class="panel panel--front" aria-label="Front of bag">
  <div class="frame"></div>
  <div class="ribbon"><span class="ribbon__text">Premium Quality</span></div>
  <div class="stars" aria-label="Five stars">
    <svg viewBox="0 0 24 24"><path d="M12 2l3 6.9 7.5.6-5.7 4.9 1.8 7.3L12 17.8 5.4 21.7l1.8-7.3L1.5 9.5 9 8.9z" fill="#6b3a12"/></svg>
    <svg viewBox="0 0 24 24"><path d="M12 2l3 6.9 7.5.6-5.7 4.9 1.8 7.3L12 17.8 5.4 21.7l1.8-7.3L1.5 9.5 9 8.9z" fill="#6b3a12"/></svg>
    <svg viewBox="0 0 24 24"><path d="M12 2l3 6.9 7.5.6-5.7 4.9 1.8 7.3L12 17.8 5.4 21.7l1.8-7.3L1.5 9.5 9 8.9z" fill="#6b3a12"/></svg>
    <svg viewBox="0 0 24 24"><path d="M12 2l3 6.9 7.5.6-5.7 4.9 1.8 7.3L12 17.8 5.4 21.7l1.8-7.3L1.5 9.5 9 8.9z" fill="#6b3a12"/></svg>
    <svg viewBox="0 0 24 24"><path d="M12 2l3 6.9 7.5.6-5.7 4.9 1.8 7.3L12 17.8 5.4 21.7l1.8-7.3L1.5 9.5 9 8.9z" fill="#6b3a12"/></svg>
  </div>
  <h1 class="brand">Kavrel<span class="brand__dot"></span></h1>
  <p class="descriptor">Arroz 100% Jasmin Perfumado</p>
  <div class="dragon-art" role="img" aria-label="Decorative dragon emblem"></div>
  <div class="window">
    <svg viewBox="0 0 494 270" preserveAspectRatio="none" role="img" aria-label="Transparent window showing the jasmine rice grains">
      <defs>
        <linearGradient id="riceWindow" x1="0" y1="0" x2="0" y2="1">
          <stop offset="0" stop-color="#f7efd9"/>
          <stop offset="1" stop-color="#d9ccaa"/>
        </linearGradient>
      </defs>
      <path d="M0 110 C150 20 330 20 494 70 L494 254 Q494 270 478 270 L16 270 Q0 270 0 254 Z" fill="url(#riceWindow)"/>
      <path d="M0 110 C150 20 330 20 494 70" fill="none" stroke="#6b3a12" stroke-width="5"/>
    </svg>
  </div>
  <div class="dish-photo" role="img" aria-label="Plate of cooked jasmine rice with vegetables and basil"></div>
</section>

<section class="panel panel--back" aria-label="Back of bag">
  <div class="frame"></div>
  <div class="map-art" role="img" aria-label="Map of the growing region with rice terraces"></div>

  <table class="nutrition">
    <caption>NUTRITION FACTS</caption>
    <tr class="per"><td>Per 100 g</td><td></td></tr>
    <tr><td>Energy</td><td>350 kcal</td></tr>
    <tr><td>Protein</td><td>7 g</td></tr>
    <tr><td>Carbohydrate</td><td>78 g</td></tr>
    <tr><td>Sugars</td><td>0.1 g</td></tr>
    <tr><td>Fat</td><td>0.6 g</td></tr>
    <tr><td>Saturates</td><td>0.2 g</td></tr>
    <tr><td>Fibre</td><td>1.3 g</td></tr>
    <tr><td>Sodium</td><td>0 mg</td></tr>
  </table>

  <ol class="steps">
    <li class="step"><span class="step__num">1</span><span class="step__text">Rinse rice in cold water</span></li>
    <li class="step"><span class="step__num">4</span><span class="step__text">Cover and simmer 15 min</span></li>
    <li class="step"><span class="step__num">2</span><span class="step__text">Add 1.5 cups water per cup</span></li>
    <li class="step"><span class="step__num">5</span><span class="step__text">Rest for 5 minutes</span></li>
    <li class="step"><span class="step__num">3</span><span class="step__text">Bring to a boil</span></li>
    <li class="step"><span class="step__num">6</span><span class="step__text">Fluff and serve</span></li>
  </ol>

  <address class="company" style="font-style:normal">
    <div class="company__name">Lusorice Trading Lda</div>
    <div>Rua das Flores 12, 4050 Porto</div>
    <div>Tel: 220 000 000</div>
    <div>info@lusorice.pt</div>
  </address>

  <p class="storage-note">For better rice, rest before serving. Store in a cool and dry place.</p>
  <p class="origin">Product of Portugal</p>

  <div class="grade">AAA</div>
</section>

</body>
</html>
```